Jewelry Shop Needs a Business Card Design

***We want a very sharp and unforgettable pantone for the Business Card. ***
***We do not want the business card or logo only in black, white and grey color!!!Please provide us a main color as our brand topic! Thanks!! ***

Mabel’s Nook is a Hong Kong based fine jewelry brand.

We want a very nice, simple and elegant business card design for Mabel's Nook Brand. The company's logo has been uploaded already.

You can design with below info:

Dorian Fung
Director
M: +852 94273658
T: +852 35820417
F: +852 35820419
E: dorian.fung@mabelsnook.example
5/F , Harbourlight Tower, 12-18 Orchid Lane, Wan Tung Kok, Kowloon, Hong Kong

Target Market(s)

Mabel’s Nook philosophy is a jewelry icon of young, creative, trendy, fashionable, stylish, energetic, and elegant. For Mabel’s Nook, jewelry is one collection of artworks, the most important items in personal life.

Industry/Entity Type

Jewelry

Requirements
Must have
• We want a very sharp and unforgettable pantone for the Business Card.

```html
<!DOCTYPE html>
<html lang="en">
<head>
<meta charset="utf-8">
<title>Mabel’s Nook — Business Card</title>
<link rel="stylesheet" href="https://fonts.googleapis.com/css2?family=Cinzel:wght@400&family=Montserrat:wght@400;600&display=swap">
<style>
  :root {
    --backdrop-top: #9a9394;
    --backdrop-bottom: #867e7f;
    --card-black: #1f1e1e;
    --brand-magenta: #d41f6c;
    --brand-magenta-deep: #a3134f;
    --ink-light: #b9b5b5;
    --ink-bright: #e9e5e4;
    --emboss: #282727;
    --emboss-shade: #141313;
  }
  html, body {
    margin: 0;
    padding: 0;
    width: 1200px;
    height: 1091px;
    overflow: hidden;
  }
  body {
    background: linear-gradient(160deg, var(--backdrop-top), var(--backdrop-bottom));
    position: relative;
    font-family: "Montserrat", sans-serif;
  }
  .card {
    position: absolute;
    width: 520px;
    height: 300px;
    background: var(--card-black);
    border-radius: 3px;
    box-shadow: 0 6px 0 var(--brand-magenta-deep), 0 18px 40px rgba(40, 30, 32, 0.35);
  }
  .card--details { left: 70px; top: 260px; }
  .card--brand { left: 610px; top: 520px; }

  .emboss-mark {
    position: absolute;
    left: 212px;
    top: 38px;
    width: 96px;
    height: 96px;
    border-radius: 50%;
    background: var(--emboss);
    box-shadow: inset 2px 2px 3px var(--emboss-shade), inset -1px -1px 2px #2f2e2e;
  }
  .holder {
    position: absolute;
    left: 40px;
    top: 150px;
    color: var(--ink-light);
  }
  .holder__name {
    margin: 0;
    font-weight: 600;
    font-size: 17px;
    letter-spacing: 0.16em;
    text-transform: uppercase;
    color: var(--brand-magenta);
  }
  .holder__role {
    margin: 2px 0 16px;
    font-size: 10px;
    letter-spacing: 0.14em;
    text-transform: uppercase;
  }
  .holder__lines {
    margin: 0;
    font-size: 10.5px;
    letter-spacing: 0.1em;
    line-height: 1.55;
  }
  .holder__email {
    margin: 14px 0 0;
    font-size: 10px;
    letter-spacing: 0.1em;
    text-transform: uppercase;
  }
  .address {
    position: absolute;
    right: 36px;
    top: 110px;
    margin: 0;
    font-size: 10.5px;
    line-height: 1.5;
    letter-spacing: 0.1em;
    text-align: right;
    text-transform: uppercase;
    color: var(--ink-light);
    font-style: normal;
  }

  .brand-disc {
    position: absolute;
    left: 205px;
    top: 40px;
    width: 110px;
    height: 110px;
    border-radius: 50%;
    background: var(--brand-magenta);
  }
  .brand-name {
    position: absolute;
    left: 0;
    right: 0;
    top: 185px;
    margin: 0;
    text-align: center;
    font-family: "Cinzel", serif;
    font-weight: 400;
    font-size: 25px;
    letter-spacing: 0.04em;
    color: var(--ink-bright);
  }
</style>
</head>
<body>
  <section class="card card--details" aria-label="Business card, contact side">
    <div class="emboss-mark"></div>
    <div class="holder">
      <h1 class="holder__name">Dorian Fung</h1>
      <p class="holder__role">Director</p>
      <p class="holder__lines">
        M. +852 94273658<br>
        T. +852 35820417<br>
        F. +852 35820419
      </p>
      <p class="holder__email">dorian.fung@mabelsnook.example</p>
    </div>
    <address class="address">
      5/F , Harbourlight<br>
      Tower, 12-18 Orchid<br>
      Lane, Wan Tung Kok,<br>
      Kowloon, Hong Kong
    </address>
  </section>

  <section class="card card--brand" aria-label="Business card, brand side">
    <div class="brand-disc"></div>
    <p class="brand-name">Mabel’s Nook</p>
  </section>
</body>
</html>
```